Brightpath Holdings Business Card

Create a two sided, high gloss, quality business card for Brightpath Holdings.

Target Market(s)

People wanting to purchase, scale, and sell businesses.

Industry/Entity Type

Entrepreneurs

Contact Information for Business Card

One line: Dana Corwell, CPA, CMA Another line: Entrepreneur & Investor Another line: Business Ownership Transition Expert Another line: Multi-State Licensed Real Estate Broker Phone 954-BRTPATH (278-7284) Email Dana@Brightpath Holdings.com Website www.Brightpath.com

Requirements
Must have
• Black Card, logo on one side, all other information on the other side including a small logo.
Nice to have
• Possibly add a tagline "Helping entrepreneurs live a life they don't need a vacation from"
Should not have
• There will not be a mailing address on these cards.

```html
<!DOCTYPE html>
<html lang="en">
<head>
<meta charset="utf-8">
<title>Brightpath Holdings Business Card</title>
<link href="https://fonts.googleapis.com/css2?family=Open+Sans:wght@400;600;700&display=swap" rel="stylesheet">
<style>
  :root {
    --page: #3a3a3c;
    --card: #050505;
    --gold: #e2b22a;
    --gold-soft: #b8912c;
    --rule: #6b5a2a;
    --text: #f2f2f2;
    --muted: #b9b9b9;
  }
  * { box-sizing: border-box; margin: 0; padding: 0; }
  html, body { width: 1200px; height: 900px; overflow: hidden; }
  body {
    background: var(--page);
    font-family: "Open Sans", Arial, sans-serif;
    position: relative;
  }
  .card {
    position: absolute;
    left: 250px;
    width: 700px;
    height: 400px;
    background: var(--card);
    box-shadow: 0 10px 30px rgba(0,0,0,.55);
  }
  .card--front { top: 40px; }
  .card--back { top: 460px; }

  /* Front */
  .portrait {
    position: absolute;
    left: 40px; top: 40px;
    width: 270px; height: 270px;
    border: 3px solid var(--gold-soft);
    background: linear-gradient(160deg, #f2f2f2 0%, #dcdcdc 55%, #2a2a2a 56%, #1a1a1a 80%, #c9a23a 100%);
  }
  .info {
    position: absolute;
    left: 340px; top: 34px; right: 36px;
    color: var(--text);
  }
  .brand {
    display: flex; align-items: center; gap: 10px;
    color: var(--gold);
    font-weight: 700;
    font-size: 26px;
    letter-spacing: .2px;
    padding-bottom: 12px;
  }
  .brand__dot {
    width: 18px; height: 18px; border-radius: 50%;
    background: var(--gold);
  }
  .rule { height: 1px; background: var(--rule); }
  .person { padding: 12px 0 14px; }
  .person__name {
    color: var(--gold);
    font-weight: 700;
    font-size: 17px;
    text-transform: uppercase;
    margin-bottom: 4px;
  }
  .person__role { font-size: 14.5px; line-height: 1.42; }
  .contact { list-style: none; padding-top: 14px; }
  .contact li {
    display: flex; align-items: center; gap: 10px;
    font-size: 14.5px; line-height: 1.65;
  }
  .contact svg { width: 15px; height: 15px; flex: none; }
  .tagline-band {
    position: absolute;
    left: 40px; right: 36px; bottom: 34px;
    border-top: 1px solid var(--rule);
    padding-top: 12px;
    color: var(--gold);
    font-size: 20px;
    font-weight: 600;
  }

  /* Back */
  .back-mark {
    position: absolute;
    left: 0; right: 0; top: 135px;
    display: flex; flex-direction: column; align-items: center;
  }
  .back-mark__brand {
    display: flex; align-items: center; gap: 14px;
    color: var(--gold);
    font-weight: 700;
    font-size: 50px;
  }
  .back-mark__dot {
    width: 30px; height: 30px; border-radius: 50%;
    background: var(--gold);
  }
  .back-mark__tagline {
    margin-top: 18px;
    color: var(--muted);
    font-size: 13px;
    font-weight: 600;
  }
</style>
</head>
<body>

<section class="card card--front">
  <div class="portrait" role="img" aria-label="Portrait photo of Dana Corwell in a dark blazer and gold blouse"></div>
  <div class="info">
    <div class="brand"><span class="brand__dot"></span>Brightpath Holdings</div>
    <div class="rule"></div>
    <div class="person">
      <p class="person__name">Dana Corwell, CPA, CMA</p>
      <p class="person__role">Entrepreneur &amp; Investor</p>
      <p class="person__role">Business Ownership Transition Expert</p>
      <p class="person__role">Multi-State Licensed Real Estate Broker</p>
    </div>
    <div class="rule"></div>
    <ul class="contact">
      <li>
        <svg viewBox="0 0 24 24" fill="none" stroke="#e2b22a" stroke-width="2" aria-hidden="true"><path d="M5 3h4l2 5-2.5 1.5a11 11 0 0 0 6 6L16 13l5 2v4a2 2 0 0 1-2 2A16 16 0 0 1 3 5a2 2 0 0 1 2-2z"/></svg>
        954-BRTPATH (278-7284)
      </li>
      <li>
        <svg viewBox="0 0 24 24" fill="none" stroke="#e2b22a" stroke-width="2" aria-hidden="true"><rect x="3" y="5" width="18" height="14" rx="1"/><path d="M3 6l9 7 9-7"/></svg>
        Dana@Brightpath Holdings.com
      </li>
      <li>
        <svg viewBox="0 0 24 24" fill="none" stroke="#e2b22a" stroke-width="2" aria-hidden="true"><circle cx="12" cy="12" r="9"/><path d="M3 12h18M12 3c3 3 3 15 0 18M12 3c-3 3-3 15 0 18"/></svg>
        www.Brightpath.com
      </li>
    </ul>
  </div>
  <p class="tagline-band">Helping entrepreneurs live a life they don't need a vacation from</p>
</section>

<section class="card card--back">
  <div class="back-mark">
    <div class="back-mark__brand"><span class="back-mark__dot"></span>Brightpath Holdings</div>
    <p class="back-mark__tagline">Helping entrepreneurs live a life they don't need a vacation from</p>
  </div>
</section>

</body>
</html>
```